Exercise Physiologist needs a Brochure

I am Exercise Physiologist providing exercise therapy for a variety of conditions. I have a logo and recent business card design. I like the black background like the front of the business cards. I have attached the flyer information required. I have also attached a few photos however they do not have to be used, happy to have no photos at all.

Industry/Entity Type

Health And Wellness

Font styles to use
Sans Serif

Requirements
Must have
• Please also add instagram @morvalecare
Nice to have
• tri-fold brochure

```html
<!DOCTYPE html>
<html lang="en">
<head>
<meta charset="utf-8">
<title>Morvale Health &amp; Rehabilitation – Exercise Physiology</title>
<link href="https://fonts.googleapis.com/css2?family=Ubuntu:ital,wght@0,400;0,500;0,700;1,400;1,500&family=Kalam:wght@400;700&display=swap" rel="stylesheet">
<style>
  :root {
    --ink: #05080d;
    --sky: #35b4e8;
    --sky-deep: #1f8fd0;
    --ocean: #0d6fb8;
    --navy: #11386a;
    --white: #ffffff;
    --text-dark: #0b0f14;
  }
  * { box-sizing: border-box; margin: 0; padding: 0; }
  html, body { width: 934px; height: 1200px; overflow: hidden; background: var(--ink); }
  .flyer {
    position: relative; width: 934px; height: 1200px; overflow: hidden;
    font-family: "Ubuntu", Arial, sans-serif; color: var(--white);
    background: var(--ink);
  }
  .backdrop {
    position: absolute; inset: 0;
    background: radial-gradient(ellipse at 35% 85%, #1d2731 0%, #0c131b 45%, var(--ink) 80%);
  }
  .script { font-family: "Kalam", "Comic Sans MS", cursive; }

  .brand { position: absolute; left: 54px; top: 54px; display: flex; align-items: center; gap: 16px; }
  .brand-dot { width: 100px; height: 100px; border-radius: 50%; background: var(--sky-deep); }
  .brand-name { font-size: 40px; font-weight: 500; color: var(--sky-deep); line-height: 1.05; }
  .brand-name span { display: block; font-size: 15px; letter-spacing: .5px; margin-top: 4px; }

  .credential-panel { position: absolute; left: 653px; top: 0; width: 224px; height: 254px; }
  .credential-text { position: absolute; left: 677px; top: 68px; width: 196px; }
  .credential-text .name { font-size: 27px; font-weight: 700; color: var(--navy); white-space: nowrap; }
  .credential-text .role { font-size: 18px; font-style: italic; font-weight: 500; color: var(--white); margin-top: 2px; }
  .credential-text .quals { font-size: 11.5px; font-style: italic; line-height: 19px; margin-top: 3px; }

  .banner { position: absolute; left: 55px; top: 204px; width: 520px; height: 64px;
    background: var(--sky); display: flex; align-items: center; padding-left: 13px; }
  .banner h1 { font-size: 36px; font-weight: 700; letter-spacing: .3px; white-space: nowrap; }

  .tagline { position: absolute; left: 55px; top: 278px; font-size: 23.5px; line-height: 33px; white-space: nowrap; }
  .tagline em { font-style: normal; color: var(--sky); }

  h2 { font-family: "Kalam", "Comic Sans MS", cursive; font-weight: 400; color: var(--sky); font-size: 27px; line-height: 32px; }
  p, li { font-size: 14.3px; line-height: 22.2px; }

  .intro { position: absolute; left: 55px; top: 372px; width: 800px; }
  .intro p { margin-top: 3px; }

  .help { position: absolute; left: 55px; top: 506px; width: 385px; }
  .help p { margin-top: 4px; margin-bottom: 22.2px; }

  .conditions { position: absolute; left: 486px; top: 504px; width: 380px; }
  .conditions ul { list-style: none; margin-top: 11px; width: 320px; }
  .conditions li { position: relative; padding-left: 20px; line-height: 23.7px; }
  .conditions li::before { content: ""; position: absolute; left: 2px; top: 10px; width: 4px; height: 4px; border-radius: 50%; background: var(--sky-deep); }
  .pull-quote { margin-top: 15px; font-family: "Kalam", cursive; font-size: 15.5px; line-height: 23.7px; width: 375px; }

  .waves { position: absolute; left: 0; top: 0; }

  .footer-call { position: absolute; left: 48px; top: 1083px; color: var(--text-dark); }
  .footer-call .prompt { font-size: 17.5px; color: var(--sky-deep); }
  .phone { display: flex; align-items: center; gap: 10px; font-size: 25px; font-weight: 700; margin-top: 2px; }
  .address { display: flex; align-items: center; gap: 14px; font-size: 14px; margin-top: 6px; padding-left: 6px; }
  .footer-links { position: absolute; left: 629px; top: 1097px; color: var(--text-dark); font-size: 15.5px; }
  .footer-links div { display: flex; align-items: center; gap: 12px; height: 37px; }
  .square-mark { width: 19px; height: 19px; background: var(--ocean); }
</style>
</head>
<body>
<div class="flyer">
  <div class="backdrop" role="img" aria-label="Dim photograph of gym equipment behind the text"></div>

  <svg class="waves" width="934" height="1200" viewBox="0 0 934 1200" aria-hidden="true">
    <path d="M0 920 Q420 1035 934 855 L934 1200 L0 1200 Z" fill="#4fb6ea"/>
    <path d="M0 935 Q430 1060 934 880 L934 1200 L0 1200 Z" fill="#1b86cf"/>
    <path d="M0 1000 Q480 1110 934 940 L934 1200 L0 1200 Z" fill="#0f6db7"/>
    <path d="M0 1015 Q500 1130 934 990 L934 1200 L0 1200 Z" fill="#ffffff"/>
    <path d="M0 1030 Q520 1140 934 1000 L934 1200 L0 1200 Z" fill="#f3f8fc"/>
  </svg>

  <div class="brand">
    <div class="brand-dot"></div>
    <div class="brand-name">Morvale<span>Health &amp; Rehabilitation</span></div>
  </div>

  <svg class="credential-panel" viewBox="0 0 224 254" aria-hidden="true">
    <path d="M0 0 H224 V254 L0 200 Z" fill="var(--sky)"/>
  </svg>
  <div class="credential-text">
    <div class="name">Claire Danvers</div>
    <div class="role">Exercise Physiologist</div>
    <div class="quals">B.AppSci – Human Mvmt<br>Grad Dip – ExRehab<br>Cert IV – Training &amp; Assessment</div>
  </div>

  <div class="banner"><h1>HEAL THROUGH MOVEMENT</h1></div>

  <div class="tagline script">
    Don’t let the right exercise but the wrong technique hinder your recovery<br>
    Discover how important <em>the correct exercise technique</em> is to your success
  </div>

  <section class="intro">
    <h2>What is an Exercise Physiologist?</h2>
    <p>Exercise Physiologists are university educated health professionals trained to provide exercise therapy for pain and injury, pre and post surgery, mental health and chronic disease. They are registered providers with TransitCover, WorkGuard, HealthCover and Department of Service Families and many Private Health funds.</p>
  </section>

  <section class="help">
    <h2>How can I help you?</h2>
    <p>I have over 13 years of experience working as an Exercise Physiologist and have been working in the sport and fitness industry since 1996. I understand that everyone’s health and exercise experience is unique and will tailor a program to suit you and your lifestyle.</p>
    <p>Managing your condition involves working with you to develop the best exercises and teaching you the correct technique essential to improve. Home and gym based programs can be provided.</p>
    <p>When appropriate I can also work with your current treating health practitioner to provide a holistic approach to your recovery.</p>
  </section>

  <section class="conditions">
    <h2>Common conditions that<br>benefit from exercise therapy</h2>
    <ul>
      <li>Back pain</li>
      <li>Joint pain</li>
      <li>Pain relating to exercise</li>
      <li>Arthritis</li>
      <li>Anxiety relating to exercise</li>
      <li>Depression and Anxiety</li>
      <li>Chronic diseases such as diabetes, heart and lung disease.</li>
      <li>Motor vehicle accidents</li>
    </ul>
    <p class="pull-quote">Performing the right exercise the wrong way can do more harm than good. I can teach you what, how and when to perform your tailored exercise program to get the best results.</p>
  </section>

  <div class="footer-call">
    <div class="prompt script">Call or email me today to see how I can help you.</div>
    <div class="phone">
      <svg width="20" height="20" viewBox="0 0 24 24" aria-hidden="true"><path fill="var(--ocean)" d="M6.6 10.8a15.1 15.1 0 0 0 6.6 6.6l2.2-2.2c.3-.3.7-.4 1-.2 1.1.4 2.3.6 3.6.6.6 0 1 .4 1 1V20c0 .6-.4 1-1 1A17 17 0 0 1 3 4c0-.6.4-1 1-1h3.5c.6 0 1 .4 1 1 0 1.3.2 2.5.6 3.6.1.3 0 .7-.2 1z"/></svg>
      0400 555 019
    </div>
    <div class="address">
      <svg width="10" height="14" viewBox="0 0 10 14" aria-hidden="true"><path fill="var(--ocean)" d="M5 0a5 5 0 0 0-5 5c0 3.8 5 9 5 9s5-5.2 5-9a5 5 0 0 0-5-5zm0 7a2 2 0 1 1 0-4 2 2 0 0 1 0 4z"/></svg>
      Gate 4, 18 Quarry Lane Northbrook (Halden Fitness)
    </div>
  </div>

  <div class="footer-links">
    <div>
      <svg width="20" height="15" viewBox="0 0 20 15" aria-hidden="true"><rect x="1" y="1" width="18" height="13" fill="none" stroke="var(--ocean)" stroke-width="2"/><path d="M1 1 L10 8 L19 1" fill="none" stroke="var(--ocean)" stroke-width="2"/></svg>
      morvalecare@mailhub.com
    </div>
    <div><span class="square-mark"></span>@morvalecare</div>
  </div>
</div>
</body>
</html>
```